Online video and marketing company business cards

Need to get some new business cards designed to fit with our new logo. The cards should be professional, clean and simple.

Cards should have:

Name
Position
2 line address
telephone
mobile
email address
web address

We need to have our logo and if possible say what we do...
ONLINE FILM PRODUCTION & STRATEGY

Industry/Entity Type

Marketing

```html
<!DOCTYPE html>
<html lang="en">
<head>
<meta charset="utf-8">
<title>Orbitreel business cards</title>
<link rel="stylesheet" href="https://fonts.googleapis.com/css2?family=Lato:wght@400;700&display=swap">
<style>
  :root {
    --navy: #0b3a62;
    --steel: #5f93ad;
    --pale-blue: #7fa9c4;
    --paper: #ececed;
    --ink: #1f2326;
    --backdrop: #d9d6d1;
  }
  * { box-sizing: border-box; margin: 0; padding: 0; }
  html, body { width: 1200px; height: 900px; overflow: hidden; }
  body {
    background: var(--backdrop);
    font-family: "Lato", sans-serif;
    position: relative;
  }
  .card {
    position: absolute;
    width: 525px;
    height: 300px;
    border-radius: 3px;
    box-shadow: 0 10px 24px rgba(0,0,0,.18);
    overflow: hidden;
  }
  /* Front */
  .card--front {
    left: 90px; top: 300px;
    background: var(--navy);
  }
  .card--front .brand {
    position: absolute;
    left: 120px; top: 92px;
    display: flex; align-items: center; gap: 14px;
  }
  .brand__dot {
    width: 52px; height: 52px; border-radius: 50%;
    background: var(--pale-blue);
  }
  .brand__name {
    font-weight: 700;
    font-size: 50px;
    letter-spacing: -1px;
    line-height: 1;
  }
  .card--front .brand__name { color: #ffffff; }
  .tagline {
    position: absolute;
    left: 0; right: 0; top: 192px;
    text-align: center;
    color: var(--pale-blue);
    font-size: 17px;
    letter-spacing: 1.5px;
    text-transform: uppercase;
  }
  /* Back */
  .card--back {
    left: 640px; top: 300px;
    background: var(--paper);
  }
  .card--back .stripe {
    position: absolute; left: 0; top: 0; bottom: 0;
    width: 18px; background: var(--navy);
  }
  .card--back .brand {
    position: absolute; left: 42px; top: 56px;
    display: flex; align-items: center; gap: 10px;
  }
  .card--back .brand__dot { width: 40px; height: 40px; background: var(--navy); }
  .card--back .brand__name { font-size: 38px; color: var(--steel); }
  .person {
    position: absolute; left: 44px; top: 150px;
  }
  .person__name { font-size: 20px; color: var(--ink); }
  .person__role {
    font-size: 13px; color: var(--navy);
    letter-spacing: .5px; text-transform: uppercase; margin-top: 2px;
  }
  .website {
    position: absolute; left: 44px; top: 236px;
    font-size: 14px; color: var(--ink);
  }
  .website span { color: var(--steel); }
  .contact {
    position: absolute; left: 310px; top: 62px;
    font-size: 12.5px; color: var(--ink); line-height: 1.45;
  }
  .contact dl { display: grid; grid-template-columns: 16px auto; }
  .contact dt { color: var(--navy); font-weight: 700; }
  .contact address { font-style: normal; margin-top: 12px; }
</style>
</head>
<body>
  <section class="card card--front" aria-label="Card front">
    <div class="brand">
      <span class="brand__dot"></span>
      <span class="brand__name">orbitreel</span>
    </div>
    <p class="tagline">Online Film Production &amp; Strategy</p>
  </section>

  <section class="card card--back" aria-label="Card back">
    <div class="stripe"></div>
    <div class="brand">
      <span class="brand__dot"></span>
      <span class="brand__name">orbitreel</span>
    </div>
    <div class="person">
      <p class="person__name">Mira Kessler</p>
      <p class="person__role">Manager</p>
    </div>
    <p class="website">www.<span>orbitreel</span>.com</p>
    <div class="contact">
      <dl>
        <dt>t</dt><dd>555-014-2288</dd>
        <dt>m</dt><dd>555-019-4471</dd>
        <dt>e</dt><dd>mira@orbitreel.com</dd>
      </dl>
      <address>18 Harbor Lane Suite 4<br>Easton CA 90210 USA</address>
    </div>
  </section>
</body>
</html>
```